Homepage and Interior Page Design for BrontaLux

We will provide all logos, graphics and images as well as a wireframe of the desired homepage layout. Deliverables should be two well formated Photoshop files will well named layers, one for the homepage and one for an interior page. The "Puzzle Animation" will be developed separately. This will be a puzzle that breaks apart and reassembles to rotate the images. Here is the old site: https://www.brontalux.example/

Target Market(s)

Small to mid sized manufacturers.

Number of Pages Required

2 page

Font styles to use
Sans Serif

Colors

Designer to choose colors to be used in the design.

Requirements
Must have
• 2 layered photoshop files ready for slicing to HTML will well labeled layers
Nice to have
• If you are interested in creating the animation as a separate project, let me know.

```html
<!DOCTYPE html>
<html lang="en">
<head>
<meta charset="utf-8">
<title>BrontaLux — Packaging and Assembly Experts</title>
<link rel="stylesheet" href="https://fonts.googleapis.com/css2?family=Montserrat:wght@400;600;700&family=Playfair+Display:ital,wght@0,400;0,700;1,400&display=swap">
<style>
  :root{
    --ink:#14172a;
    --navy:#1c2036;
    --navy-deep:#11131f;
    --footer:#0b0c12;
    --cyan:#27c3e6;
    --red:#e0322b;
    --white:#ffffff;
    --muted:#8d93a8;
    --line:#2d3350;
  }
  *{box-sizing:border-box;margin:0;padding:0}
  html,body{width:778px;height:1200px;overflow:hidden}
  body{font-family:"Montserrat",sans-serif;background:var(--navy);color:var(--white);position:relative}

  /* top bar */
  .topbar{position:absolute;top:0;left:0;width:778px;height:44px;background:var(--navy-deep)}
  .topbar .phone{position:absolute;left:70px;top:15px;font-size:8px;letter-spacing:1px;color:var(--muted);display:flex;align-items:center;gap:6px;white-space:nowrap}
  .brand-box{position:absolute;left:337px;top:0;width:104px;height:58px;background:var(--white);display:flex;align-items:center;justify-content:center;z-index:3}
  .brand{font-family:"Montserrat",sans-serif;font-weight:700;font-size:15px;color:var(--cyan)}
  .top-tools{position:absolute;right:70px;top:13px;display:flex;gap:8px;align-items:center}
  .top-tools .search{font-size:7px;color:var(--muted);border-bottom:1px solid var(--line);width:60px;padding-bottom:2px}
  .dot{width:12px;height:12px;border-radius:50%;background:var(--line);flex:none}

  /* nav */
  .mainnav{position:absolute;top:44px;left:0;width:778px;height:30px;background:var(--ink);display:flex;justify-content:center}
  .mainnav a{flex:none;white-space:nowrap;font-size:5.5px;font-weight:600;letter-spacing:.4px;color:#c9cde0;text-decoration:none;padding:0 8px;line-height:30px}
  .mainnav a.active{background:var(--cyan);color:var(--white)}
  .mainnav .spacer{flex:none;width:112px}

  /* hero */
  .hero{position:absolute;top:74px;left:0;width:778px;height:341px;background:var(--white)}
  .hero-photo{position:absolute;left:246px;top:0;width:532px;height:341px;background:linear-gradient(120deg,#0d1d3d 0%,#1f4a86 40%,#5d8fcf 60%,#17325f 100%)}
  .hero-grid{position:absolute;left:246px;top:0}
  .hero-copy{position:absolute;left:70px;top:120px;width:165px}
  .hero-copy h1{font-size:12px;font-weight:700;letter-spacing:1px;line-height:1.4;color:var(--ink);white-space:nowrap}
  .hero-copy p{font-size:5.5px;letter-spacing:1.6px;color:#555;margin-top:4px;white-space:nowrap}
  .btn{display:inline-block;font-size:6.5px;font-weight:700;letter-spacing:1px;color:var(--white);padding:6px 13px;white-space:nowrap}
  .btn-red{background:var(--red);margin-top:14px}
  .btn-cyan{background:var(--cyan)}

  /* success */
  .success{position:absolute;top:415px;left:0;width:778px;height:207px;background:var(--navy)}
  .success .kicker{position:absolute;left:140px;top:90px;font-size:6.5px;letter-spacing:1.5px;color:#c9cde0}
  .success h2{position:absolute;left:140px;top:102px;font-family:"Playfair Display",serif;font-weight:400;font-size:15px;letter-spacing:1.5px;color:var(--cyan);white-space:nowrap}
  .success .body{position:absolute;left:140px;top:126px;width:150px;font-size:6px;line-height:1.6;color:var(--muted)}
  .years{position:absolute;left:430px;top:60px;width:190px;height:100px}
  .years .num{position:absolute;left:0;top:0;font-family:"Playfair Display",serif;font-style:italic;font-size:96px;line-height:1;color:rgba(255,255,255,.12)}
  .years .label{position:absolute;left:92px;top:44px;font-size:17px;letter-spacing:3px;color:#c9cde0}
  .years .sub{position:absolute;left:92px;top:66px;font-size:6px;letter-spacing:1.5px;color:var(--muted);white-space:nowrap}

  /* services */
  .services{position:absolute;top:622px;left:0;width:778px;height:375px;background:linear-gradient(180deg,#3d434f 0%,#5a5f68 45%,#2c3038 100%)}
  .services-band{position:absolute;left:142px;top:58px;width:493px;height:22px;background:var(--cyan)}
  .cards{position:absolute;left:150px;top:62px;width:478px;display:flex;justify-content:space-between}
  .card{width:104px;text-align:center}
  .card .photo{width:104px;height:112px;border:3px solid var(--white)}
  .card h3{font-family:"Playfair Display",serif;font-weight:400;font-size:11px;letter-spacing:1px;line-height:1.15;color:var(--white);margin-top:14px;height:44px}
  .card p{font-size:5.5px;line-height:1.6;color:#d5d8e2;margin:6px 4px 14px}

  /* footer */
  .footer{position:absolute;top:997px;left:0;width:778px;height:203px;background:var(--footer);text-align:center}
  .footer .brand{display:block;margin-top:28px;font-size:16px;color:var(--white)}
  .footer .blurb{width:340px;margin:14px auto 0;font-size:5.5px;line-height:1.7;color:var(--muted)}
  .socials{display:flex;justify-content:center;gap:22px;margin-top:22px}
  .socials .dot{width:11px;height:11px;background:#4a5068}
  .footnav{display:flex;justify-content:center;gap:20px;margin-top:16px;font-size:5.5px;letter-spacing:.8px;color:#b7bccc;white-space:nowrap}
  .copy{position:absolute;left:0;right:0;bottom:16px;font-size:5px;color:#5d6277}
</style>
</head>
<body>
  <header class="topbar">
    <div class="phone">
      <svg width="8" height="8" viewBox="0 0 24 24"><path d="M6.6 10.8a15 15 0 0 0 6.6 6.6l2.2-2.2c.3-.3.7-.4 1-.2 1.1.4 2.3.6 3.6.6.6 0 1 .4 1 1V20c0 .6-.4 1-1 1A17 17 0 0 1 3 4c0-.6.4-1 1-1h3.5c.6 0 1 .4 1 1 0 1.3.2 2.5.6 3.6.1.3 0 .7-.2 1z" fill="#8d93a8"/></svg>
      (555) 010-2040
    </div>
    <div class="brand-box"><span class="brand">BrontaLux</span></div>
    <div class="top-tools">
      <span class="search">Search</span>
      <span class="dot"></span><span class="dot"></span><span class="dot"></span>
    </div>
  </header>

  <nav class="mainnav">
    <a class="active" href="#">CONTRACT PACKAGING</a>
    <a href="#">PRODUCT ASSEMBLY</a>
    <span class="spacer"></span>
    <a href="#">CUSTOM PALLETS &amp; CRATES</a>
    <a href="#">INVENTORY MANAGEMENT &amp; FULFILLMENT</a>
    <a href="#">ABOUT</a>
    <a href="#">CONTACT</a>
  </nav>

  <section class="hero">
    <div class="hero-photo" role="img" aria-label="Welder at work with bright sparks, shown as puzzle tiles"></div>
    <svg class="hero-grid" width="532" height="341" aria-hidden="true">
      <g stroke="rgba(255,255,255,.35)" stroke-width="1">
        <line x1="53" y1="0" x2="53" y2="341"/><line x1="106" y1="0" x2="106" y2="341"/><line x1="159" y1="0" x2="159" y2="341"/>
        <line x1="212" y1="0" x2="212" y2="341"/><line x1="265" y1="0" x2="265" y2="341"/><line x1="318" y1="0" x2="318" y2="341"/>
        <line x1="371" y1="0" x2="371" y2="341"/><line x1="424" y1="0" x2="424" y2="341"/><line x1="477" y1="0" x2="477" y2="341"/>
        <line x1="0" y1="53" x2="532" y2="53"/><line x1="0" y1="106" x2="532" y2="106"/><line x1="0" y1="159" x2="532" y2="159"/>
        <line x1="0" y1="212" x2="532" y2="212"/><line x1="0" y1="265" x2="532" y2="265"/>
      </g>
      <g fill="#ffffff">
        <rect x="0" y="0" width="53" height="53"/><rect x="424" y="0" width="108" height="53"/>
        <rect x="0" y="212" width="53" height="53"/><rect x="371" y="212" width="53" height="53"/>
        <rect x="477" y="159" width="55" height="53"/><rect x="0" y="265" width="106" height="76"/>
      </g>
    </svg>
    <div class="hero-copy">
      <h1>PACKAGING AND<br>ASSEMBLY EXPERTS</h1>
      <p>LOREM IPSUM DOLOR SIT AMET</p>
      <span class="btn btn-red">READ MORE</span>
    </div>
  </section>

  <section class="success">
    <p class="kicker">LOREM IPSUM DOLOR SIT AMET</p>
    <h2>SECRET OF SUCCESS</h2>
    <p class="body">We pack, assemble and ship products for manufacturers across the region with care and speed.</p>
    <div class="years">
      <span class="num">36</span>
      <span class="label">YEARS</span>
      <span class="sub">OF EXPERIENCE</span>
    </div>
  </section>

  <section class="services" role="img" aria-label="Blurred warehouse interior background">
    <div class="services-band"></div>
    <div class="cards">
      <article class="card">
        <div class="photo" role="img" aria-label="Packaged goods on a workbench" style="background:linear-gradient(160deg,#8a6a4a,#3e3a36)"></div>
        <h3>CONTRACT<br>PACKAGING</h3>
        <p>We pack and assemble your goods on time, every time.</p>
        <span class="btn btn-cyan">READ MORE</span>
      </article>
      <article class="card">
        <div class="photo" role="img" aria-label="Product assembly line" style="background:linear-gradient(160deg,#b9bcc2,#5b6068)"></div>
        <h3>PRODUCT<br>ASSEMBLY</h3>
        <p>We pack and assemble your goods on time, every time.</p>
        <span class="btn btn-cyan">READ MORE</span>
      </article>
      <article class="card">
        <div class="photo" role="img" aria-label="Stacked wooden crates and pallets" style="background:linear-gradient(160deg,#a07a4e,#4a3826)"></div>
        <h3>CUSTOM<br>PALLETS &amp;<br>CRATES</h3>
        <p>We pack and assemble your goods on time, every time.</p>
        <span class="btn btn-cyan">READ MORE</span>
      </article>
      <article class="card">
        <div class="photo" role="img" aria-label="Warehouse shelving with inventory" style="background:linear-gradient(160deg,#5b6f8a,#26303f)"></div>
        <h3>INVENTORY<br>MANAGEMENT<br>&amp; FULFILLMENT</h3>
        <p>We pack and assemble your goods on time, every time.</p>
        <span class="btn btn-cyan">READ MORE</span>
      </article>
    </div>
  </section>

  <footer class="footer">
    <span class="brand">BrontaLux</span>
    <p class="blurb">BrontaLux is a contract packaging and assembly partner for small and mid sized manufacturers.</p>
    <div class="socials"><span class="dot"></span><span class="dot"></span><span class="dot"></span><span class="dot"></span></div>
    <div class="footnav">
      <span>HOME</span><span>CONTRACT PACKAGING</span><span>PRODUCT ASSEMBLY</span><span>CUSTOM PALLETS</span><span>INVENTORY</span><span>ABOUT US</span><span>CONTACT US</span><span>SITEMAP</span>
    </div>
    <p class="copy">© 2024 BrontaLux. All rights reserved.</p>
  </footer>
</body>
</html>
```